Australian Online Training Organisation needs a Website Design

We need a Web Design ideally using a Wordpress Divi template which will represent an Australian Online Training Company.

(Pendlow Online Training)

The website will represent a range of short courses with an emphasis on business, brightnet, leadership etc.

The website will 'shell out' to the third party portal where 'bookings' occur. I am imaging a fantastic looking web design with perhaps 5-6 pages.

I am wondering if a selection of courses including the below list can be incorporated?

The variety of courses include :

Workplace Safety
Sales Training
Leadership
Process Management
Problem Solving
Project Management
Business Planning
Meetings and Events
Emotional Intelligence
Human Resources
Administrative Essentials
Customer Service
Career Development
Conflict Resolution
Train the Trainer
Supervisors and Managers
Internet marketing
Communications
Team Building
Marketing
Finance
Writing
Job Search Skills
Public Speaking
Negotiation Skills
Talent Management
Brightnet Deskline 2016
BDS Preparation for Deskline 2010
Deskline 2013
Deskline 2010
Upgrading to Deskline 2010
Computer Fundamentals
Upgrading to Deskline 2007
Deskline 2003
Deskline 2002
Varlo Deskline X3
Core Essentials
Deskline 2007

Thank you so much for all of the amazing designs we received. We were so happy with so many elements that it was very hard to choose. Our top two were very hard to decide upon but we look forward to working more with both of these talents into the future. Thank you again.

Target Market(s)

Professionals, students and workers who would like to improve their skills with online training in over 500 + courses -

Industry/Entity Type

It Company

Number of Pages Required

5+ page

Font styles to use
Sans Serif

Colors
3276b5
faa54b
0355a3
fac994

Requirements
Must have
• Ideally would use Wordpress theme (Divi for example or other)
• Very smart front end
• Will upload logo soon
• (Pendlow Online Training)
• pendlowonlinetraining.edu.au
• Graphics of 'people' pretty important - with a variety of ages.
Nice to have
• Interesting page
• National presence
• A bit University looking
• Professional
• Graphics of people
• Blog
• Graphics of people
• Age range from job seekers, to business folk, etc

```html
<!DOCTYPE html>
<html lang="en">
<head>
<meta charset="utf-8">
<title>Pendlow Online Training</title>
<link href="https://fonts.googleapis.com/css2?family=Titillium+Web:wght@200;300;400;600;700&display=swap" rel="stylesheet">
<style>
:root{
  --blue:#0355a3;
  --blue-mid:#3276b5;
  --orange:#faa54b;
  --orange-light:#fac994;
  --dark:#2b2d30;
  --white:#ffffff;
  --ink:#1d2a3a;
}
*{box-sizing:border-box;margin:0;padding:0}
html,body{width:1200px;height:3516px;overflow:hidden}
body{font-family:"Titillium Web",Arial,sans-serif;color:var(--white);position:relative;background:var(--white)}
section,header,footer{position:absolute;left:0;width:1200px;overflow:hidden}
.abs{position:absolute}

/* top bar */
.topbar{top:0;height:28px;background:var(--blue);font-size:11px;z-index:3}
.topbar .contact-line{left:235px;top:6px}
.topbar .contact-line span{margin-right:14px}
.topbar .shop-links{right:235px;top:6px}
.topbar .shop-links span{margin-left:16px}

/* hero */
.hero{top:0;height:633px}
.hero-photo{position:absolute;inset:0;background:radial-gradient(ellipse at 75% 35%,#f4f3f0 0%,#d9d7d1 40%,#a9a79f 100%)}
.hero-photo::after{content:"";position:absolute;left:0;right:0;bottom:0;height:220px;background:linear-gradient(to bottom,rgba(200,198,192,0),rgba(120,118,112,.55))}
.brand{left:232px;top:92px;display:flex;align-items:center;gap:10px}
.brand-mark{width:22px;height:22px;background:var(--blue)}
.brand-name{font-size:30px;font-weight:600;color:var(--blue);letter-spacing:1px}
.main-nav{left:448px;top:108px;display:flex;gap:30px;font-size:13px;color:var(--ink)}
.main-nav a{color:var(--ink);text-decoration:none;padding:3px 10px}
.main-nav a.active{background:var(--blue);color:var(--white);border-radius:3px;font-weight:600}
.hero-title{right:300px;top:300px;text-align:right;color:#111}
.hero-title .line1{font-size:64px;font-weight:200;line-height:68px;letter-spacing:-1px}
.hero-title .line2{font-size:72px;font-weight:700;line-height:76px}
.hero-title .line2 b{color:var(--blue)}
.hero-sub{left:300px;width:600px;top:463px;text-align:center;font-size:13px;color:var(--blue);letter-spacing:2px;font-weight:600}
.slider-dots{left:530px;top:572px;display:flex;gap:6px}
.slider-dots i{width:34px;height:4px;background:rgba(255,255,255,.6)}
.slider-dots i.on{background:var(--blue-mid)}

/* welcome */
.welcome{top:633px;height:609px}
.welcome-photo{position:absolute;inset:0;background:linear-gradient(100deg,#d98a35 0%,#f2a24c 35%,#f5b063 60%,#d08a3a 100%)}
.welcome-photo::after{content:"";position:absolute;inset:0;background:rgba(250,165,75,.55)}
.welcome-title{left:0;width:1200px;top:90px;text-align:center;font-size:38px;font-weight:300;color:var(--blue)}
.welcome-title b{color:var(--white);font-weight:700}
.welcome-copy{left:280px;width:640px;top:165px;text-align:center;font-size:15px;line-height:20px}
.welcome-copy p{margin-bottom:20px}

/* shared headings */
.section-title{left:0;width:1200px;text-align:center;font-size:36px;font-weight:300}
.section-title b{font-weight:700}
.divider{left:400px;width:400px;height:20px}

/* courses */
.courses{top:1242px;height:785px;background:radial-gradient(ellipse at 20% 30%,#1a6ac0 0%,var(--blue) 55%,#02478a 100%)}
.courses .section-title{top:45px}
.courses-intro{left:400px;width:400px;top:143px;text-align:center;font-size:10px;line-height:13px;font-weight:600}
.course-card{width:220px;text-align:center}
.course-photo{width:220px;height:108px;background:linear-gradient(135deg,#c9d3dd,#6f8295)}
.course-name{margin-top:10px;font-size:16px;font-weight:700;color:var(--orange)}
.course-text{margin-top:4px;font-size:10px;line-height:13px;padding:0 10px}
.pager{left:555px;top:725px}

/* testimonials */
.testimonials{top:2027px;height:774px}
.testimonials-photo{position:absolute;inset:0;background:linear-gradient(120deg,#c27a2c 0%,#f0a04a 40%,#f7b469 70%,#d88f3e 100%)}
.testimonials-photo::after{content:"";position:absolute;inset:0;background:rgba(250,165,75,.6)}
.testimonials .section-title{top:50px;color:var(--white)}
.testimonials .section-title b{color:var(--blue)}
.testimonials-intro{left:380px;width:440px;top:140px;text-align:center;font-size:12px;line-height:17px;font-weight:600;color:var(--ink)}
.timeline-line{left:609px;top:215px;width:2px;height:460px;background:var(--blue)}
.timeline-node{width:22px;height:22px;background:var(--blue);transform:rotate(45deg);border:2px solid var(--orange-light)}
.quote{width:320px;color:var(--ink);font-size:10px;line-height:13px}
.quote .who{font-size:11px;font-weight:700}
.quote .role{font-size:9px;color:var(--blue);margin-bottom:8px}
.quote.left{text-align:right}
.avatar{width:116px;height:116px;border-radius:50%;border:4px solid var(--white);background:linear-gradient(135deg,#e6e2dc,#9a948c)}
.load-more{left:557px;top:693px;width:108px;height:34px;background:var(--blue);font-size:11px;font-weight:700;text-align:center;line-height:34px}

/* contact */
.contact{top:2801px;height:663px}
.contact-photo{position:absolute;inset:0;background:linear-gradient(110deg,#3b3a38 0%,#242528 45%,#3a3733 100%)}
.contact .section-title{top:50px}
.contact .section-title b{color:var(--blue-mid)}
.contact-intro{left:370px;width:460px;top:147px;text-align:center;font-size:10px;line-height:13px}
.info{width:240px;text-align:center;font-size:13px;line-height:17px}
.info .icon{width:42px;height:42px;border-radius:50%;background:var(--white);margin:0 auto 8px;display:flex;align-items:center;justify-content:center}
.info .label{font-size:12px;font-weight:600;margin-bottom:2px}
.field{height:44px;background:var(--blue);border:1px solid #5f93c9;font-size:11px;padding:12px 10px;color:var(--white)}
.send{left:525px;top:575px;width:148px;height:42px;background:var(--white);color:var(--blue);font-size:13px;font-weight:700;text-align:center;line-height:42px}

/* footer */
.site-footer{top:3464px;height:52px;background:var(--blue);font-size:10px}
.site-footer .copy{left:235px;top:20px}
</style>
</head>
<body>

<header class="topbar">
  <div class="abs contact-line"><span>&#9742; 1300-555-0188</span><span>&#9993; contact@pendlowonlinetraining.edu.au</span></div>
  <div class="abs shop-links"><span>Shop &#9662;</span><span>My Account</span><span>Check Out</span><span>0 Items</span></div>
</header>

<section class="hero">
  <div class="hero-photo" role="img" aria-label="Photo of a hand touching a glowing network over a laptop keyboard"></div>
  <div class="abs brand"><span class="brand-mark"></span><span class="brand-name">PENDLOW</span></div>
  <nav class="abs main-nav">
    <a class="active" href="#">HOME</a><a href="#">ABOUT US</a><a href="#">COURSES</a><a href="#">CONTACT</a><a href="#">SIGN IN</a><a href="#">REGISTER</a>
  </nav>
  <div class="abs hero-title">
    <div class="line1">DELIVERING OVER</div>
    <div class="line2"><b>600</b> WELL PRICED</div>
  </div>
  <div class="abs hero-sub">accessible short courses in a variety of skill sets online directly to you.</div>
  <div class="abs slider-dots"><i></i><i class="on"></i><i></i><i></i></div>
</section>

<section class="welcome">
  <div class="welcome-photo" role="img" aria-label="Photo of students studying on laptops in a classroom"></div>
  <h1 class="abs welcome-title">WELCOME TO <b>PENDLOW ONLINE TRAINING</b></h1>
  <div class="abs welcome-copy">
    <p>Pendlow Online Training is one of Australia's leading provider of flexible and affordable online continuing professional development programs, with over 600 online courses now available.</p>
    <p>Our range of self-paced online courses are delivered completely online via our e-learning system <b>24/7</b>.</p>
    <p>We offer a range of popular online courses in accounting, finance, bookkeeping, management, marketing, information technology, project management and more. Our online courses are industry relevant and are designed to help you achieve your career goals.</p>
    <p>Pendlow specialise in online Brightnet product training – prefect<br>Studying online allows you to balance study with your existing work and home life commitments. With Pendlow Online you can train in your own space from work, at home or anywhere you have an internet connection.</p>
    <p>Our All-Inclusive Fee Guarantee ensures that you receive all course materials, 12 months' e-learning access with no more to pay. Free extensions are also available if you need extra time to complete your course.</p>
  </div>
</section>

<section class="courses">
  <h2 class="abs section-title">OUR <b>TRAINING COURCES</b></h2>
  <svg class="abs divider" style="top:103px" viewBox="0 0 400 20"><line x1="0" y1="10" x2="185" y2="10" stroke="#fff" stroke-width="1.5"/><circle cx="200" cy="10" r="7" fill="none" stroke="#fff" stroke-width="2.5"/><line x1="215" y1="10" x2="400" y2="10" stroke="#fff" stroke-width="1.5"/></svg>
  <p class="abs courses-intro">Short courses built for busy people, written by industry experts and delivered online so you can learn at your own pace, anywhere.</p>

  <div class="abs course-card" style="left:235px;top:218px"><div class="course-photo" role="img" aria-label="Photo of a sales team meeting"></div><div class="course-name">Sales Training</div><p class="course-text">Practical lessons, real workplace examples and short assessments help you build skills you can use straight away in your role.</p></div>
  <div class="abs course-card" style="left:490px;top:218px"><div class="course-photo" role="img" aria-label="Photo of a business leadership team"></div><div class="course-name">Leadership</div><p class="course-text">Practical lessons, real workplace examples and short assessments help you build skills you can use straight away in your role.</p></div>
  <div class="abs course-card" style="left:745px;top:218px"><div class="course-photo" role="img" aria-label="Photo of process planning with digital icons"></div><div class="course-name">Process Management</div><p class="course-text">Practical lessons, real workplace examples and short assessments help you build skills you can use straight away in your role.</p></div>
  <div class="abs course-card" style="left:235px;top:458px"><div class="course-photo" role="img" aria-label="Photo of a tired worker at a desk"></div><div class="course-name">Problem Solving</div><p class="course-text">Practical lessons, real workplace examples and short assessments help you build skills you can use straight away in your role.</p></div>
  <div class="abs course-card" style="left:490px;top:458px"><div class="course-photo" role="img" aria-label="Photo of a project team working around a table"></div><div class="course-name">Project Management</div><p class="course-text">Practical lessons, real workplace examples and short assessments help you build skills you can use straight away in your role.</p></div>
  <div class="abs course-card" style="left:745px;top:458px"><div class="course-photo" role="img" aria-label="Photo of a business planning presentation"></div><div class="course-name">Business Planning</div><p class="course-text">Practical lessons, real workplace examples and short assessments help you build skills you can use straight away in your role.</p></div>

  <svg class="abs pager" width="90" height="16" viewBox="0 0 90 16"><path d="M7 3 2 8l5 5" fill="none" stroke="#fff" stroke-width="2"/><circle cx="20" cy="8" r="4.5" fill="#fff"/><circle cx="34" cy="8" r="4.5" fill="none" stroke="#fff" stroke-width="1.5"/><circle cx="48" cy="8" r="4.5" fill="none" stroke="#fff" stroke-width="1.5"/><circle cx="62" cy="8" r="4.5" fill="none" stroke="#fff" stroke-width="1.5"/><path d="M77 3l5 5-5 5" fill="none" stroke="#fff" stroke-width="2"/></svg>
</section>

<section class="testimonials">
  <div class="testimonials-photo" role="img" aria-label="Photo of smiling students together"></div>
  <h2 class="abs section-title">STUDENTS <b>TESTIMONIALS</b></h2>
  <svg class="abs divider" style="top:107px" viewBox="0 0 400 20"><line x1="0" y1="10" x2="185" y2="10" stroke="#0355a3" stroke-width="1.5"/><circle cx="200" cy="10" r="7" fill="none" stroke="#fff" stroke-width="2.5"/><line x1="215" y1="10" x2="400" y2="10" stroke="#0355a3" stroke-width="1.5"/></svg>
  <p class="abs testimonials-intro">Hear from learners who grew their careers with us. Real stories from people studying online across Australia.</p>
  <div class="abs timeline-line"></div>

  <div class="abs timeline-node" style="left:599px;top:223px"></div>
  <div class="abs quote left" style="left:270px;top:225px"><div class="who">JHONSON DOE</div><div class="role">Sales Manager</div><p>The course was clear, practical and easy to fit around my work. I finished in weeks and used the skills straight away with my team and clients.</p></div>
  <div class="abs avatar" style="left:641px;top:218px" role="img" aria-label="Portrait of a male student"></div>

  <div class="abs timeline-node" style="left:599px;top:348px"></div>
  <div class="abs avatar" style="left:462px;top:360px" role="img" aria-label="Portrait of a female student"></div>
  <div class="abs quote" style="left:640px;top:350px"><div class="who">JANE DOE</div><div class="role">Office Manager</div><p>The course was clear, practical and easy to fit around my work. I finished in weeks and used the skills straight away with my team and clients.</p></div>

  <div class="abs timeline-node" style="left:599px;top:503px"></div>
  <div class="abs quote left" style="left:270px;top:505px"><div class="who">RICHARD DOE</div><div class="role">Team Leader</div><p>The course was clear, practical and easy to fit around my work. I finished in weeks and used the skills straight away with my team and clients.</p></div>
  <div class="abs avatar" style="left:641px;top:508px" role="img" aria-label="Portrait of a male student with glasses"></div>

  <div class="abs load-more">LOAD MORE</div>
</section>

<section class="contact">
  <div class="contact-photo" role="img" aria-label="Photo of two people talking at a laptop, darkened"></div>
  <h2 class="abs section-title">FEEL FREE <b>TO ASK US</b></h2>
  <svg class="abs divider" style="top:104px" viewBox="0 0 400 20"><line x1="0" y1="10" x2="185" y2="10" stroke="#3276b5" stroke-width="1.5"/><circle cx="200" cy="10" r="7" fill="none" stroke="#fff" stroke-width="2.5"/><line x1="215" y1="10" x2="400" y2="10" stroke="#3276b5" stroke-width="1.5"/></svg>
  <p class="abs contact-intro">Have a question about a course, enrolment or fees? Send us a message and our friendly team will reply within one business day.</p>

  <div class="abs info" style="left:227px;top:233px">
    <div class="icon"><svg width="20" height="20" viewBox="0 0 20 20"><path d="M10 2 1 10h3v8h5v-5h2v5h5v-8h3z" fill="#2b2d30"/></svg></div>
    <div class="label">ADDRESS</div><div>2870 Harbour Road Suite 140<br>Carlton, VIC 3053</div>
  </div>
  <div class="abs info" style="left:480px;top:233px">
    <div class="icon"><svg width="20" height="20" viewBox="0 0 20 20"><ellipse cx="10" cy="9" rx="8" ry="6.5" fill="#2b2d30"/><path d="M5 13l-2 5 6-3z" fill="#2b2d30"/></svg></div>
    <div class="label">MAIL</div><div>contact@pendlowonlinetraining.edu.au</div>
  </div>
  <div class="abs info" style="left:730px;top:233px">
    <div class="icon"><svg width="20" height="20" viewBox="0 0 20 20"><path d="M5 2l3 4-2 2c1 2 4 5 6 6l2-2 4 3-2 3C9 18 2 11 2 4z" fill="#2b2d30"/></svg></div>
    <div class="label">PHONE</div><div>1300-555-0142</div>
  </div>

  <div class="abs field" style="left:232px;top:359px;width:233px">Enter Name</div>
  <div class="abs field" style="left:482px;top:359px;width:233px">Enter Mail</div>
  <div class="abs field" style="left:733px;top:359px;width:233px">Enter Subject</div>
  <div class="abs field" style="left:232px;top:422px;width:734px;height:134px">Enter Message</div>
  <div class="abs send">Send Message</div>
</section>

<footer class="site-footer">
  <div class="abs copy">© Copyright 2016 <b>pendlowonlinetraining.edu.au</b> All Rights Reserved.</div>
</footer>

</body>
</html>
```